Gutscheine für Massage Salon
Zielgruppe
Es handelt dich um einen Massage Salon mit dem Namen „Lindwerk Oase Massage“ Zielgruppe im Prinzip alle Menschen. Es werden verschiedene Massagearten angeboten, von Traditioneller Chinesischer, Thai bis Gesichtsmassage!. Auf der Webseite ersichtlich.
Aufgabenstellung
Der Gutschein soll hochwertig erscheinen und im Querformat mit Kuvert überreicht werden. Auch das Kuvert sollte bedruckt werden. Inhalte wie Gültigkeit, Gutscheinwert, Platz für Unterschrift, Ausstellungsdatun und Stempel sollen vorhanden sein. Platz für den Namen der den Gutschein als Geschenk erhält! Gutschein beidseitig bedruckt. In Bezug suf die Gültigkeit, bitte ich zu berücksichtigen, das lt. Gesetz der Gutschein 5 Jahre ab Kaufdatum gültig ist.

```html
<!DOCTYPE html>
<html lang="de">
<head>
<meta charset="utf-8">
<title>Gutschein – Lindwerk Oase Massage</title>
<link rel="stylesheet" href="https://fonts.googleapis.com/css2?family=Arimo&family=Cinzel+Decorative&family=Cinzel:wght@700&display=swap">
<style>
  :root {
    --field: rgba(255, 219, 189, 0.93);
    --veil: rgba(170, 160, 165, 0.38);
    --cream: #f1e6cf;
    --gold: #f3dfb0;
    --ink: #1d1411;
    --dash: #a89a90;
    --white: #ffffff;
  }
  * { margin: 0; padding: 0; box-sizing: border-box; }
  html, body { width: 1200px; height: 583px; overflow: hidden; background: #1a120e; }
  .voucher {
    position: relative;
    width: 1200px;
    height: 583px;
    overflow: hidden;
    font-family: "Arimo", Arial, sans-serif;
  }
  .room-scene {
    position: absolute; inset: 0;
    background:
      radial-gradient(ellipse 160px 120px at 405px 150px, rgba(255, 214, 140, 0.55), transparent 70%),
      linear-gradient(180deg, transparent 55%, rgba(140, 40, 25, 0.55) 70%, rgba(90, 45, 25, 0.85) 100%),
      linear-gradient(90deg, #1e1512 0%, #3a2a22 35%, #4a3a30 60%, #2d221d 80%, #3e3530 100%);
  }
  .title {
    position: absolute; left: 78px; top: 22px;
    font-family: "Cinzel Decorative", "Cinzel", serif;
    font-size: 88px; font-weight: 400;
    letter-spacing: 1px;
    color: var(--cream);
    line-height: 1;
  }
  .field {
    position: absolute;
    background: var(--field);
    border-radius: 2px;
    display: flex; align-items: center;
    padding: 0 40px 0 34px;
    font-size: 23px; color: var(--ink);
  }
  .field-line {
    flex: 1;
    margin: 14px 0 0 18px;
    border-bottom: 1.5px dashed var(--dash);
  }
  .field-recipient { left: 91px; top: 147px; width: 492px; height: 90px; }
  .field-sender { left: 617px; top: 147px; width: 492px; height: 90px; padding-left: 28px; }
  .field-value { left: 205px; top: 276px; width: 791px; height: 90px; }
  .currency {
    position: absolute; right: 38px; top: 30px;
    font-family: "Cinzel", serif; font-weight: 400;
    font-size: 26px; color: var(--ink);
  }
  .cash-note {
    position: absolute; left: 414px; top: 375px;
    font-size: 14px; color: var(--white);
  }
  .sign-box, .valid-box {
    position: absolute;
    background: var(--veil);
    border-bottom: 1.5px dashed rgba(255,255,255,0.75);
  }
  .sign-box { left: 80px; top: 384px; width: 290px; height: 151px; }
  .valid-box { left: 469px; top: 470px; width: 281px; height: 65px; }
  .box-label {
    position: absolute; top: 539px;
    font-size: 17px; color: var(--white);
  }
  .label-sign { left: 85px; }
  .label-valid { left: 468px; }
  .brand {
    position: absolute; left: 880px; top: 330px; width: 290px;
    display: flex; flex-direction: column; align-items: center; gap: 14px;
    font-family: "Cinzel", serif; font-weight: 700;
    color: var(--gold); text-align: center;
    font-size: 34px; line-height: 1.05;
  }
  .brand-dot { width: 70px; height: 70px; border-radius: 50%; border: 3px solid var(--gold); }
</style>
</head>
<body>
<main class="voucher">
  <div class="room-scene" role="img" aria-label="Foto eines warm beleuchteten Massageraums mit Liege, gerollten Handtüchern und Lampe"></div>

  <h1 class="title">GUTSCHEIN</h1>

  <div class="field field-recipient">für:<span class="field-line"></span></div>
  <div class="field field-sender">von:<span class="field-line"></span></div>
  <div class="field field-value">im Wert von:<span class="field-line"></span><span class="currency">EURO</span></div>

  <p class="cash-note">Eine Barauszahlung des Gutscheins ist nicht möglich!</p>

  <div class="sign-box"></div>
  <span class="box-label label-sign">Unterschrift/ Stempel</span>
  <div class="valid-box"></div>
  <span class="box-label label-valid">Gültig bis</span>

  <div class="brand">
    <span class="brand-dot"></span>
    <span class="brand-name">LINDWERK OASE MASSAGE</span>
  </div>
</main>
</body>
</html>
```